Postcard design to acquire new clients for my Property Management Company

I'm looking for a postcard design that I can send to prospective clients detailing information about my company and services.
Postcard should be eye catching and contain information from www.brightkeyrentals-example.com. I've provided a few screen shots for the most important information and my logo.
Target Market(s)
Real Estate
Industry/Entity Type
Real Estate
Font styles to use
Sans Serif
Requirements
Must have
- Must be eye catching!! this will be a direct mail piece - I'd like for the card to be read and not tossed in the trash immediately.
Design que from the logo.
A place to write / print the receipts name and address.
our physical address - 2287 Marble Lane, Lubbock, TX 79555.
Should not have
- the contact information on the business card is not accurate - please use info from website.

```html
<!DOCTYPE html>
<html lang="en">
<head>
<meta charset="utf-8">
<title>BrightKey Rentals – Direct Mail Postcard</title>
<link href="https://fonts.googleapis.com/css2?family=Montserrat:wght@500;600;700;800;900&family=Raleway:wght@400;500;700&display=swap" rel="stylesheet">
<style>
:root{
  --navy:#0b4a7c;
  --navy-dark:#0a3f6b;
  --ink:#3a3a3a;
  --muted:#555;
  --stage:#7b7b7b;
  --paper:#ffffff;
  --rule:#c9c9c9;
  --panel:#f1f1f1;
  --pill:#a3a3a3;
}
*{margin:0;padding:0;box-sizing:border-box}
html,body{width:1200px;height:811px;overflow:hidden;background:var(--stage)}
body{position:relative;font-family:'Montserrat',sans-serif;color:var(--ink)}
.stage-title{position:absolute;top:34px;left:0;width:1238px;text-align:center;color:#fff;font-weight:700;font-size:22px;letter-spacing:.3px}
.side-label{position:absolute;top:742px;width:200px;text-align:center;color:#fff;font-weight:700;font-size:22px}
.side-label.front{left:236px}
.side-label.back{left:759px}

.card{position:absolute;top:80px;width:455px;height:643px;background:var(--paper);overflow:hidden}
.card.front{left:118px}
.card.back{left:628px}

/* FRONT */
.brand-band{position:absolute;left:0;top:0;width:87px;height:100%;background:var(--navy)}
.top-rule{position:absolute;left:87px;top:15px;width:368px;height:1px;background:var(--rule)}
.brand-name{position:absolute;left:87px;width:368px;top:33px;text-align:center;color:var(--navy);font-weight:700;font-size:30px;letter-spacing:5px;line-height:1.2}
.brand-name span{display:block;font-size:15px;letter-spacing:4.5px;font-weight:700}
.hero-photo{position:absolute;left:142px;top:88px;width:313px;height:203px;
  background:linear-gradient(180deg,#f3eef4 0%,#d9cfe0 30%,#5d6b86 55%,#3e4c66 75%,#8c97aa 100%)}
.service-panel{position:absolute;left:0;top:92px;width:142px;height:456px;background:var(--paper);border-radius:0 24px 24px 0;box-shadow:2px 2px 6px rgba(0,0,0,.12)}
.service-heading{position:absolute;left:19px;top:13px;font-weight:800;color:var(--navy);font-size:15px;letter-spacing:.5px}
.service-heading::after{content:"";position:absolute;left:0;top:24px;width:109px;height:3px;background:#999}
.service{position:absolute;left:17px;display:flex;align-items:center;gap:9px;height:30px}
.service svg{width:27px;height:27px;fill:var(--navy);flex:none}
.service p{font-weight:700;font-size:11.5px;line-height:13.5px;color:#3d3d3d;letter-spacing:.4px}

.pricing{position:absolute;left:150px;top:291px;width:287px;height:289px;border:1.5px solid var(--rule);border-top:none;border-left:none;border-radius:0 0 34px 0}
.plan{position:absolute;left:0;width:277px;padding:0 8px}
.plan.featured{background:var(--panel);border-top:1.5px solid var(--rule);border-bottom:1.5px solid var(--rule)}
.plan-head{display:flex;justify-content:space-between}
.plan-name{font-weight:800;color:var(--navy);font-size:16px;letter-spacing:.5px;line-height:18px}
.plan-price{font-weight:800;color:var(--navy);font-size:17px;width:90px;line-height:18px}
.plan-sub{display:flex;justify-content:space-between;font-family:'Raleway',sans-serif;font-size:9.5px;line-height:12px;color:var(--muted)}
.plan-sub em{font-style:normal;color:var(--navy);width:90px}
.plan-body{font-family:'Raleway',sans-serif;font-size:8.9px;line-height:11.8px;letter-spacing:-.1px;color:#444;margin-top:6px}

.contact-pill{position:absolute;left:13px;top:559px;width:137px;height:27px;background:var(--pill);border-radius:14px 0 0 14px;color:#fff;font-weight:800;font-size:15px;letter-spacing:1px;line-height:27px;padding-left:18px}
.contact-pill::after{content:"";position:absolute;right:0;top:27px;border-left:8px solid transparent;border-top:8px solid var(--pill)}
.contact-line{position:absolute;left:96px;top:605px;display:flex;gap:10px;align-items:center;color:var(--navy);font-weight:700;font-size:11.5px;letter-spacing:.2px}
.contact-line svg{width:13px;height:13px;fill:#8a8a8a;vertical-align:-2px;margin-right:2px}

/* BACK */
.back-photo{position:absolute;left:0;top:0;width:455px;height:293px;
  background:linear-gradient(180deg,#b7b3cf 0%,#dcc6cc 22%,#59627e 45%,#3c4660 65%,#3b6a94 85%,#2e5f8e 100%)}
.back-headline{position:absolute;right:28px;top:214px;text-align:right;color:#fff;font-weight:700;font-size:20.5px;line-height:25px}
.back-subline{position:absolute;right:27px;top:266px;color:#fff;font-family:'Raleway',sans-serif;font-size:11.5px}
.address-lines{position:absolute;left:27px;top:350px;width:181px}
.address-lines i{display:block;height:1.5px;background:var(--rule);margin-bottom:27.3px}
.stamp-divider{position:absolute;left:233px;top:321px;width:1.5px;height:306px;background:var(--rule)}
.back-brand{position:absolute;left:31px;top:516px;width:190px;color:var(--navy);font-weight:700;font-size:21px;letter-spacing:3.5px;line-height:24px}
.back-brand span{display:block;font-size:10px;letter-spacing:3px;line-height:12px}
.back-address{position:absolute;left:31px;top:572px;font-weight:700;font-size:12.5px;line-height:13.5px;color:#585858}
.back-web{position:absolute;left:31px;top:607px;width:195px;font-weight:700;font-size:8.5px;color:#585858;white-space:nowrap}
</style>
</head>
<body>
<div class="stage-title">POSTCARD SIZE:&nbsp; 105W X 148H MM</div>

<section class="card front">
  <div class="brand-band"></div>
  <div class="top-rule"></div>
  <div class="brand-name">BRIGHTKEY<span>RENTALS</span></div>
  <div class="hero-photo" role="img" aria-label="Photo of a two-storey grey house with garage at dusk"></div>

  <aside class="service-panel">
    <h2 class="service-heading">Our Service</h2>
    <div class="service" style="top:52px"><svg viewBox="0 0 24 24"><path d="M12 3 1 12h3v9h6v-6h4v6h6v-9h3z"/></svg><p>Property<br>Marketing</p></div>
    <div class="service" style="top:103px"><svg viewBox="0 0 24 24"><circle cx="8" cy="8" r="4"/><circle cx="17" cy="8" r="3.5"/><path d="M0 20c0-4 4-7 8-7s8 3 8 7zM14 13c4 0 10 2 10 6v1h-7c0-3-1-5-3-7z"/></svg><p>Tenant<br>Screening</p></div>
    <div class="service" style="top:155px"><svg viewBox="0 0 24 24"><path d="M13 2h-2v2.2C8 4.7 6.5 6.5 6.5 8.6c0 2.6 2.2 3.6 5 4.3 2.3.6 3 1.2 3 2.2s-1.1 1.8-2.7 1.8c-1.8 0-2.8-.8-3-2.1H6.3c.2 2.4 2 3.900 4.7 4.300V21h2v-2.1c2.9-.5 4.5-2.2 4.5-4.3 0-2.8-2.4-3.8-5-4.4-2.2-.5-2.8-1.1-2.8-2s.9-1.7 2.4-1.7 2.4.7 2.6 1.8h2.5C17 6.2 15.4 4.6 13 4.2z"/></svg><p>Rent<br>Collection</p></div>
    <div class="service" style="top:206px"><svg viewBox="0 0 24 24"><path d="M9 2h7l6 5-2 2-4-3-2 2-8 14-3-2 8-13-3-3z"/></svg><p>Maintenance</p></div>
    <div class="service" style="top:255px"><svg viewBox="0 0 24 24"><path d="M14 2a8 8 0 1 1-5 14.3L3.7 21.6 2.3 20.2 7.6 14.9A8 8 0 0 1 14 2zm0 3a5 5 0 1 0 0 10 5 5 0 0 0 0-10z"/></svg><p>Property<br>Inspections</p></div>
    <div class="service" style="top:305px"><svg viewBox="0 0 24 24"><path d="M2 3h2v17h18v2H2zM6 12h2v6H6zm4-4h2v10h-2zm4 3h2v7h-2zm4-6h2v13h-2z"/></svg><p>Financial<br>Reporting</p></div>
    <div class="service" style="top:357px"><svg viewBox="0 0 24 24"><path d="M12 1 3 5v6c0 6 4 10.5 9 12 5-1.5 9-6 9-12V5zm0 3v16c-3.5-1.3-6-4.8-6-9V7z"/></svg><p>Evictions</p></div>
    <div class="service" style="top:408px"><svg viewBox="0 0 24 24"><path d="M11 2h2v3l7 1-3 7a3.5 3.5 0 0 0 7 0l-3-7h-1l-7-1v14h5v2H6v-2h5V6L4 7l3 6a3.5 3.5 0 0 1-7 0l3-7zM3 8.5 1.5 12.5h3zm18 0-1.5 4h3z"/></svg><p>Legal<br>Guidance</p></div>
  </aside>

  <div class="pricing">
    <div class="plan" style="top:10px">
      <div class="plan-head"><h3 class="plan-name">Lease Only</h3><span class="plan-price">9%</span></div>
      <div class="plan-sub"><span>- You Just Need Tenants -</span><em>of annual lease</em></div>
      <p class="plan-body">Professional Photography | Marketing &amp; Advertising | Property Showings | Tenant Screening &amp; Qualifications | Lease Execution | Move In Coordination</p>
    </div>
    <div class="plan featured" style="top:95px;height:108px;padding-top:9px">
      <div class="plan-head"><h3 class="plan-name">Full Service</h3><span class="plan-price">10%</span></div>
      <div class="plan-sub"><span>- Our Most Popular -</span><em>of monthly rent</em></div>
      <p class="plan-body">Includes Leasing Service | 24/7 Emergency Response | Move In &amp; Out Inspections | Professional Lease Enforcement Schedule &amp; Oversee all Repairs | Pay all Invoices | Monthly &amp; Year End Statements | Annual Market Rent Analysis</p>
    </div>
    <div class="plan" style="top:212px">
      <div class="plan-head"><h3 class="plan-name">Premium Service</h3><span class="plan-price">12%</span></div>
      <div class="plan-sub"><span>- Our Premier Service -</span><em>of monthly rent</em></div>
      <p class="plan-body">Includes Full Service Features | Professional Video Marketing Home Warranty Coordination | Tenant Retention Program</p>
    </div>
  </div>

  <div class="contact-pill">Contact Us:</div>
  <div class="contact-line">
    <span><svg viewBox="0 0 24 24"><path d="M6.6 10.8a15 15 0 0 0 6.6 6.6l2.2-2.2c.3-.3.7-.4 1-.2 1.1.4 2.3.6 3.6.6.6 0 1 .4 1 1V20c0 .6-.4 1-1 1A17 17 0 0 1 3 4c0-.6.4-1 1-1h3.5c.6 0 1 .4 1 1 0 1.300.2 2.500.6 3.600.1.300 0 .700-.2 1z"/></svg>(806) 555-0147</span>
    <span><svg viewBox="0 0 24 24"><path d="M2 5h20v14H2zm2 2v.5l8 5 8-5V7zm0 3v7h16v-7l-8 5z"/></svg>info@brightkeyrentals-example.com</span>
  </div>
</section>

<section class="card back">
  <div class="back-photo" role="img" aria-label="Photo of a modern two-storey house with lit windows at sunset"></div>
  <h2 class="back-headline">CHOOSE THE RIGHT<br>PROPERTY MANAGEMENT SYSTEM</h2>
  <p class="back-subline">Selecting the wrong manager could be your costliest mistake ever.</p>
  <div class="address-lines"><i></i><i></i><i></i><i></i><i></i><i></i></div>
  <div class="stamp-divider"></div>
  <div class="back-brand">BRIGHTKEY<span>RENTALS</span></div>
  <p class="back-address">2287 MARBLE LANE,<br>LUBBOCK, TX 79555</p>
  <p class="back-web">WWW.BRIGHTKEYRENTALS-EXAMPLE.COM</p>
</section>

<div class="side-label front">FRONT</div>
<div class="side-label back">BACK</div>
</body>
</html>
```